Need a business card layout made

Need to make Business card layout. I am going to use bramble cards and have my logo already made. Would like something simple but nice. I have uploaded my logo but I am not set on this color scheme. I would like to see some different color options. Please use mark lewin info for the layout and I will select a winner based on layout and will change after that.
Mark Lewin
Owner
555-318-472
marklewin@quillorb.example

```html
<!DOCTYPE html>
<html lang="en">
<head>
<meta charset="utf-8">
<title>Harlow Building Group – Business Card</title>
<link href="https://fonts.googleapis.com/css2?family=Roboto:wght@400;700;900&display=swap" rel="stylesheet">
<style>
  :root {
    --bg: #3a3c40;
    --card: #ffffff;
    --orange: #d35a25;
    --navy: #1e2a5e;
    --ink: #1d1d1f;
    --muted: #555a60;
  }
  * { margin: 0; padding: 0; box-sizing: border-box; }
  html, body { width: 1200px; height: 900px; overflow: hidden; }
  body {
    background: var(--bg);
    font-family: "Roboto", Arial, sans-serif;
    position: relative;
  }
  .card {
    position: absolute;
    width: 560px;
    height: 320px;
    background: var(--card);
    border-radius: 26px;
    overflow: hidden;
  }
  .card--front { left: 120px; top: 110px; }
  .card--back { left: 520px; top: 470px; }

  .brand {
    color: var(--orange);
    font-weight: 900;
    text-transform: uppercase;
    display: flex;
    align-items: center;
    gap: 12px;
    white-space: nowrap;
  }
  .brand__mark {
    background: var(--navy);
    flex: none;
  }
  .card--front .brand {
    position: absolute;
    left: 0; right: 0; top: 128px;
    justify-content: center;
    font-size: 34px;
    letter-spacing: 0.5px;
  }
  .card--front .brand__mark { width: 26px; height: 26px; }
  .card--front .brand-rule {
    position: absolute;
    left: 90px; right: 90px; top: 184px;
    height: 2px;
    background: var(--orange);
  }

  .card--back .brand {
    position: absolute;
    right: 40px; top: 46px;
    font-size: 18px;
    gap: 8px;
  }
  .card--back .brand__mark { width: 14px; height: 14px; }
  .card--back .brand-rule {
    position: absolute;
    right: 40px; top: 74px;
    width: 240px;
    height: 1.5px;
    background: var(--orange);
  }

  .wave { position: absolute; inset: 0; width: 560px; height: 320px; }

  .contact { position: absolute; left: 40px; top: 160px; }
  .contact__name { font-size: 24px; font-weight: 700; color: var(--ink); }
  .contact__role { font-size: 15px; color: var(--muted); margin-top: 10px; margin-left: 18px; }
  .contact__list { list-style: none; margin-top: 28px; }
  .contact__item {
    display: flex; align-items: center; gap: 10px;
    font-size: 15px; color: var(--muted);
    margin-bottom: 10px;
  }
  .contact__icon { width: 16px; height: 16px; fill: var(--navy); flex: none; }
</style>
</head>
<body>

  <section class="card card--front" aria-label="Card front">
    <div class="brand"><span class="brand__mark"></span>Harlow Building Group</div>
    <div class="brand-rule"></div>
  </section>

  <section class="card card--back" aria-label="Card back">
    <svg class="wave" viewBox="0 0 560 320" aria-hidden="true">
      <path d="M560 120 C520 160 490 210 455 260 C430 292 400 312 360 320 L560 320 Z" fill="var(--orange)"/>
      <path d="M560 150 C515 175 490 215 460 262 C440 292 415 310 385 320 L560 320 Z" fill="var(--navy)"/>
      <path d="M560 185 C530 200 510 230 485 268 C468 294 450 310 425 320 L560 320 Z" fill="var(--orange)"/>
    </svg>

    <div class="brand"><span class="brand__mark"></span>Harlow Building Group</div>
    <div class="brand-rule"></div>

    <div class="contact">
      <div class="contact__name">Mark Lewin</div>
      <div class="contact__role">Owner</div>
      <ul class="contact__list">
        <li class="contact__item">
          <svg class="contact__icon" viewBox="0 0 24 24" aria-hidden="true"><path d="M6.6 10.8a15.1 15.1 0 0 0 6.6 6.6l2.2-2.2a1 1 0 0 1 1-.25 11.4 11.4 0 0 0 3.6.57 1 1 0 0 1 1 1V20a1 1 0 0 1-1 1A17 17 0 0 1 3 4a1 1 0 0 1 1-1h3.5a1 1 0 0 1 1 1c0 1.25.2 2.45.57 3.6a1 1 0 0 1-.25 1z"/></svg>
          555-318-472
        </li>
        <li class="contact__item">
          <svg class="contact__icon" viewBox="0 0 24 24" aria-hidden="true"><path d="M2 5h20v14H2z M3.5 6.5 12 13l8.5-6.5" fill="var(--navy)" stroke="#fff" stroke-width="1.5"/></svg>
          marklewin@quillorb.example
        </li>
      </ul>
    </div>
  </section>

</body>
</html>
```